Quellmont Haus National Website

We need a website to match our Logo. We will be selling american made vapeing Oils, batteries, Cartomizers, Clearomizers. We have a wharehouse location with couches, TVs streaming clipora, vending machine, and the worlds first flavor mixing bar. We have the lowest priced high grade oils. We will send pictures of the location. Relaxed atmoshpere and no lines for purchase. VIP cards for regulars.

(PLEASE KNOW THAT THE LOGO IS THE UPPER RIGHT LOGO ONLY OF THE FOUR ON THE FILE I ATTACHED)
Updates

Keep in mind we are are only looking for concept and a non coded website

Please know that we are looking for a non coded website

Industry/Entity Type

Purchase

Requirements
Must have
• Online cart, Blog,

```html
<!DOCTYPE html>
<html lang="en">
<head>
<meta charset="utf-8">
<title>Quellmont Haus – Batteries</title>
<link href="https://fonts.googleapis.com/css2?family=Arimo:ital,wght@0,400;0,700;1,700&display=swap" rel="stylesheet">
<style>
:root{
  --black:#000;
  --panel:#1b1b1b;
  --panel-dark:#0d0d0d;
  --green:#8cc63f;
  --white:#fff;
  --grey-text:#e6e6e6;
  --footer:#333;
}
*{box-sizing:border-box;margin:0;padding:0}
html,body{width:853px;height:1200px;overflow:hidden;background:var(--black)}
body{position:relative;font-family:"Arimo",Arial,sans-serif;color:var(--white)}
.abs{position:absolute}
.header-band{left:0;top:43px;width:853px;height:77px;background:linear-gradient(#2a2a28,#0a0a0a 70%,#000)}
.main-nav{left:338px;top:22px;height:20px;font-size:10.5px}
.main-nav a{color:var(--white);text-decoration:none;position:absolute;top:0;line-height:20px;white-space:nowrap}
.main-nav .current{background:var(--green);color:#000;padding:0 6px;left:0}
.cart{left:667px;top:10px;width:84px;text-align:center;font-size:10px;white-space:nowrap}
.cart svg{display:block;margin:0 auto 1px}
.brand{left:110px;top:50px;font-size:27px;color:var(--white);font-weight:400;letter-spacing:-.5px;white-space:nowrap}
.login-box{left:574px;top:43px;width:165px;height:84px;background:var(--green);color:var(--white);font-size:7px;font-weight:700;white-space:nowrap}
.login-box .row{position:absolute;display:flex;align-items:center}
.login-box .label{width:48px;text-align:right}
.login-box .field{width:94px;height:10px;background:var(--white);margin-left:4px}
.login-box .btn{background:var(--white);color:#000;width:46px;height:12px;text-align:center;line-height:12px;margin-left:8px}
.social{width:12px;height:12px;background:var(--white);margin-left:6px}
.panel{left:106px;top:120px;width:633px;height:1004px;background:linear-gradient(#252525,var(--panel) 8%,var(--panel) 88%,var(--panel-dark))}
.page-title{left:136px;top:134px;font-size:24px;font-weight:700}
.title-rule{left:136px;top:172px;width:201px;height:5px;background:var(--green)}
.section-title{font-size:20px;font-weight:700;font-style:italic;white-space:nowrap}
.copy{font-size:9.9px;line-height:18px;color:var(--grey-text)}
.photo{border:2px solid var(--white);border-radius:2px}
.divider{left:136px;width:574px;height:0;border-top:2px dashed var(--green)}
.back{left:667px;top:1082px;width:42px;height:16px;background:var(--white);color:#000;font-size:9px;font-weight:700;text-align:center;line-height:16px}
.footer-rule{left:0;top:1138px;width:853px;height:12px;background:var(--green)}
.footer{left:0;top:1150px;width:853px;height:50px;background:var(--footer)}
.call{left:106px;top:1165px;font-size:17px;font-weight:700;white-space:nowrap}
.foot-links{left:324px;top:1168px;font-size:8.5px;white-space:nowrap}
.copyright{left:368px;top:1184px;font-size:8px;white-space:nowrap}
.foot-brand{left:607px;top:1160px;font-size:19px;color:var(--white);white-space:nowrap}
</style>
</head>
<body>
<div class="abs header-band"></div>

<nav class="abs main-nav">
  <a class="current" href="#">HOME</a>
  <a href="#" style="left:60px">ABOUT US</a>
  <a href="#" style="left:132px">SHOP</a>
  <a href="#" style="left:185px">BLOG</a>
  <a href="#" style="left:237px">CONTACT US</a>
</nav>

<div class="abs cart">
  <svg width="20" height="18" viewBox="0 0 20 18" fill="none" stroke="#8cc63f" stroke-width="1.8">
    <path d="M1 2h3l2.5 9h10l2-6H5.5"/><circle cx="8" cy="15" r="1.5"/><circle cx="15" cy="15" r="1.5"/>
  </svg>
  ONLINE CART
</div>

<div class="abs brand">Quellmont Haus</div>

<div class="abs login-box">
  <div class="row" style="left:4px;top:8px"><span class="label">EMAIL :</span><span class="field"></span></div>
  <div class="row" style="left:4px;top:22px"><span class="label">PASSWORD :</span><span class="field"></span></div>
  <div class="row" style="left:22px;top:38px"><span>Forgot your password?</span><span class="btn">LOGIN</span></div>
  <div class="row" style="left:72px;top:60px"><span>FOLLOW US</span><span class="social"></span><span class="social"></span></div>
</div>

<div class="abs panel"></div>

<h1 class="abs page-title">BATTERIES</h1>
<div class="abs title-rule"></div>

<div class="abs photo" role="img" aria-label="Car batteries with yellow tops in a workshop" style="left:136px;top:198px;width:228px;height:152px;background:linear-gradient(135deg,#5b7f9a,#c9b24a 45%,#3d3f42)"></div>
<h2 class="abs section-title" style="left:403px;top:196px">Powering The World</h2>
<p class="abs copy" style="left:403px;top:229px;width:308px">Lorem Ipsum is simply dummy text of the printing and typesetting industry. Lorem Ipsum has been the industry's standard dummy text ever since the 1500s, when an unknown printer took a galley of type and scrambled it to make a type specimen book. It has survived not only five centuries, but also the leap into electronic typesetting, remaining essentially unchanged. It was popularised in the 1960s with the release of Velmark sheets containing Lorem Ipsum passages, and more recently</p>

<div class="abs divider" style="top:381px"></div>

<h2 class="abs section-title" style="left:149px;top:403px">Fast Charging!</h2>
<p class="abs copy" style="left:149px;top:434px;width:308px">Lorem Ipsum is simply dummy text of the printing and typesetting industry. Lorem Ipsum has been the industry's standard dummy text ever since the 1500s, when an unknown printer took a galley of type and scrambled it to make a type specimen book. It has survived not only five centuries, but also the leap into electronic typesetting, remaining essentially unchanged. It was popularised in the 1960s with the release of Velmark sheets containing Lorem Ipsum passages, and more recently</p>
<div class="abs photo" role="img" aria-label="Rows of cylindrical battery cells seen from above" style="left:485px;top:406px;width:227px;height:152px;background:radial-gradient(circle at 40% 45%,#d9c9a8,#8a7a5c 55%,#2d2a24)"></div>

<div class="abs divider" style="top:583px"></div>

<div class="abs" role="img" aria-label="Technician holding a car battery and jumper cables" style="left:136px;top:612px;width:181px;height:156px;background:radial-gradient(ellipse at 50% 55%,#e0c84a,#c8c8c8 45%,#fff 75%)"></div>
<h2 class="abs section-title" style="left:403px;top:609px">Get Product Support</h2>
<p class="abs copy" style="left:403px;top:641px;width:308px">Lorem Ipsum is simply dummy text of the printing and typesetting industry. Lorem Ipsum has been the industry's standard dummy text ever since the 1500s, when an unknown printer took a galley of type and scrambled it to make a type specimen book. It has survived not only five centuries, but also the leap into electronic typesetting, remaining essentially unchanged. It was popularised in the 1960s with the release of Velmark sheets containing Lorem Ipsum passages, and more recently</p>

<div class="abs divider" style="top:794px"></div>

<h2 class="abs section-title" style="left:149px;top:822px">Batteries &amp; Chargers</h2>
<p class="abs copy" style="left:149px;top:855px;width:322px">Lorem Ipsum is simply dummy text of the printing and typesetting industry. Lorem Ipsum has been the industry's standard dummy text ever since the 1500s, when an unknown printer took a galley of type and scrambled it to make a type specimen book. It has survived not only five centuries, but also the leap into electronic typesetting, remaining essentially unchanged. It was popularised in the 1960s with the release of Velmark sheets containing Lorem Ipsum passages, and more recently with desktop publishing software like Orrin LayoutDesk including versions of Lorem Ipsum.</p>
<div class="abs" role="img" aria-label="Black car battery with red and blue terminals" style="left:485px;top:822px;width:225px;height:200px;background:radial-gradient(ellipse at 50% 55%,#2a2a2a,#555 50%,#fff 72%)"></div>

<div class="abs back">BACK</div>

<div class="abs footer-rule"></div>
<footer class="abs footer"></footer>
<div class="abs call">CALL US : 140.372.118</div>
<div class="abs foot-links">HOME &nbsp;|&nbsp; ABOUT US &nbsp;|&nbsp; SHOP &nbsp;|&nbsp; BLOG &nbsp;|&nbsp; CONTACT US</div>
<div class="abs copyright">© 2013 All RIGHTS RESERVED</div>
<div class="abs foot-brand">Quellmont Haus</div>
</body>
</html>
```